I need a very simple web page/site for my business

I have recently commissioned a logo and letterhead, I simply need someone to design a webpage/site that builds on this with a creative design and places for page titles along with descriptions of the services I offer on each page and contact details etc. I would imagine a cover page with two to three sub-pages at the most. i.e. a Home page, then "About As", "Services Offered" and "Contact and Support" pages. The Red on White design is the primary one while the Red on Black one can be used secondarily or at the bottom of pages etc, however the designer thinks best. The design should convey professionalism, technical expertise, and timeliness from a number of suitably qualified medical practitioners. If need be I can provide the necessary text, otherwise an option that allows me to fill this in afterwards would be ideal. I am not sure of the practicality of that. The principal type of work done will be clinical analysis and report writing involving clinical trials, and clinical data that support the use of drugs and medical devices in humans. Also any consultation work that requires medical analysis and critique and formal report writing, such as safety analysis, clinical trial design, or essentially anything for which expert medical commentary is required.

```html
<!DOCTYPE html>
<html lang="en">
<head>
<meta charset="utf-8">
<title>Arden Clinical — Home</title>
<link rel="stylesheet" href="https://fonts.googleapis.com/css2?family=Arimo:wght@400;700&display=swap">
<style>
  :root {
    --page-black: #000000;
    --sheet-white: #ffffff;
    --bar-dark: #222222;
    --accent-red: #e0181f;
    --brand-red: #b3121c;
    --accent-purple: #8a50f0;
    --body-grey: #666666;
    --photo-top: #dfe6ee;
    --photo-bottom: #4f79b4;
  }
  * { box-sizing: border-box; margin: 0; padding: 0; }
  html, body {
    width: 1046px; height: 1200px; overflow: hidden;
    background: var(--page-black);
    font-family: "Arimo", Arial, sans-serif;
  }
  .site {
    position: absolute; left: 23px; top: 20px;
    width: 1000px; height: 806px;
    background: var(--sheet-white);
  }
  .nav-bar {
    position: absolute; left: 0; top: 94px; width: 1000px; height: 31px;
    background: var(--bar-dark);
  }
  .nav-list {
    position: absolute; left: 222px; top: 0; height: 31px;
    display: flex; gap: 35px; list-style: none; align-items: center;
  }
  .nav-list a {
    color: var(--sheet-white); text-decoration: none;
    font-size: 15px;
  }
  .nav-list a.is-current { color: var(--accent-red); }
  .brand-box {
    position: absolute; left: 14px; top: 18px; width: 190px; height: 145px;
    background: var(--sheet-white); border: 2px solid var(--bar-dark);
    display: flex; align-items: center; justify-content: center;
  }
  .brand-name {
    display: flex; align-items: center; gap: 8px;
    color: var(--brand-red); font-size: 20px; font-weight: 400; line-height: 1;
  }
  .brand-mark { width: 12px; height: 12px; background: var(--brand-red); flex: none; }
  .feature-card {
    position: absolute; left: 8px; top: 225px; width: 331px; height: 430px;
    background: var(--accent-purple); padding: 20px 20px 0 20px; color: var(--sheet-white);
  }
  .feature-photo {
    width: 291px; height: 190px;
    background: linear-gradient(180deg, var(--photo-top) 0%, #a7b9d1 45%, var(--photo-bottom) 100%);
  }
  .feature-title {
    font-weight: 400; font-size: 27px; line-height: 33px; margin-top: 14px;
  }
  .feature-text { font-size: 12.4px; line-height: 21.7px; margin-top: 20px; }
  .info-col { position: absolute; top: 347px; width: 220px; }
  .info-col.services { left: 378px; }
  .info-col.support { left: 630px; }
  .info-title {
    color: var(--accent-purple); font-weight: 400; font-size: 19px; line-height: 24px;
  }
  .info-text {
    color: var(--body-grey); font-size: 12.5px; line-height: 21.8px; margin-top: 10px;
  }
  .read-more {
    display: inline-block; margin-top: 16px; width: 106px; height: 34px;
    border: 1px solid #b9b9c8; color: var(--accent-purple);
    font-size: 13px; line-height: 32px; text-align: center; text-decoration: none;
  }
  .site-footer {
    position: absolute; left: -4px; top: 704px; width: 1004px; height: 102px;
    background: var(--bar-dark); color: var(--sheet-white); font-size: 13px;
  }
  .footer-copy { position: absolute; left: 40px; top: 44px; }
  .footer-contact { position: absolute; right: 42px; top: 43px; }
  .footer-contact .sep { margin: 0 7px; }
</style>
</head>
<body>
  <div class="site">
    <header>
      <nav class="nav-bar">
        <ul class="nav-list">
          <li><a class="is-current" href="#">HOME</a></li>
          <li><a href="#">ABOUT</a></li>
          <li><a href="#">SERVICES</a></li>
          <li><a href="#">CONTACT&amp;SUPPORT</a></li>
        </ul>
      </nav>
      <div class="brand-box">
        <div class="brand-name"><span class="brand-mark"></span>Arden Clinical</div>
      </div>
    </header>

    <main>
      <section class="feature-card">
        <div class="feature-photo" role="img" aria-label="Photo of a team of medical practitioners in scrubs and white coats"></div>
        <h2 class="feature-title">ENDORSEMENT<br>REVIEW</h2>
        <p class="feature-text">Lorem ipsum dolor sit amet, consectetur adipisicing elit, sed do eiusmod tempor incididunt ut labore et dolore magna aliqua. Duis aute irure dolor in reprehenderit in voluptate velit esse cillum dolore eu fugiat nulla pariatur.</p>
      </section>

      <section class="info-col services">
        <h3 class="info-title">SERVICES</h3>
        <p class="info-text">Lorem ipsum dolor sit amet, consectetur adipisicing elit, sed do eiusmod tempor incididunt ut labore et dolore magna aliqua. Duis aute irure dolor in reprehenderit in voluptate velit esse cillum dolore eu fugiat nulla pariatur.</p>
        <a class="read-more" href="#">READ MORE</a>
      </section>

      <section class="info-col support">
        <h3 class="info-title">SUPPORT</h3>
        <p class="info-text">Lorem ipsum dolor sit amet, consectetur adipisicing elit, sed do eiusmod tempor incididunt ut labore et dolore magna aliqua. Duis aute irure dolor in reprehenderit in voluptate velit esse cillum dolore eu fugiat nulla pariatur.</p>
        <a class="read-more" href="#">READ MORE</a>
      </section>
    </main>

    <footer class="site-footer">
      <div class="footer-copy">© All Rights Reserved</div>
      <div class="footer-contact">ADMINEMAIL@ARDENCLINICAL.COM<span class="sep">|</span>1-800-555-014200<span class="sep">|</span>NETWORK</div>
    </footer>
  </div>
</body>
</html>
```